Mergers and Acquisitions Business Seeks Fresh Website Design

IMPORTANT: Please only design the Homepage, for the contest. If you win the contest, you will design the inner pages, as see in the attached document 'Brevka 2025 website wireframes."
Design a new website for Brevka at brevka.global. Maintaining current Impact and Open Sans fonts, or using open-source alternatives from Google Fonts.
Enhance the design with a premium feel, impactful visuals, and dynamic content. We want the new design to focus on generating high-quality inquiries, strong calls to action, and consistent branding.
Industry/Entity Type
Mergers and Acquisitions
Number of Pages Required
5+ page
Font styles to use
Other font styles liked:
- See Website Brief file
Requirements
Must have
- Consistency in layout, colours, fonts and overall design
Should not have
- Very bright colours, hard to read fonts, unlicensed images and fonts

```html
<!DOCTYPE html>
<html lang="en">
<head>
<meta charset="utf-8">
<title>Brevka — Deal Origination</title>
<link href="https://fonts.googleapis.com/css2?family=Poppins:wght@300;400;500;600;700&display=swap" rel="stylesheet">
<style>
:root{
  --purple:#54215f;
  --purple-dark:#451a4f;
  --yellow:#f6c200;
  --pink:#d43ae0;
  --ink:#2b2b2b;
  --muted:#7a7a7a;
  --light:#f3f6fa;
  --stage:#808080;
  --white:#ffffff;
}
*{margin:0;padding:0;box-sizing:border-box}
html,body{width:1200px;height:1200px;overflow:hidden}
body{background:var(--stage);font-family:"Poppins",sans-serif;color:var(--ink)}
.page{position:absolute;left:484px;top:20px;width:375px;height:1848px;background:var(--white);transform:scale(.62108);transform-origin:0 0;overflow:hidden}
.abs{position:absolute}
.center{left:0;right:0;text-align:center}
.section-title{position:absolute;left:0;right:0;text-align:center;font-size:9.5px;color:var(--purple);font-weight:500}
.section-title b{font-weight:500;color:var(--purple)}
.rule{position:absolute;height:2px;background:var(--yellow);width:40px;left:167.5px}

/* header */
.brand{left:40px;top:-2px;font-size:27px;font-weight:700;color:var(--purple);letter-spacing:-.5px}
.util{right:38px;top:5px;font-size:5.5px;font-weight:600;display:flex;gap:6px;align-items:center}
.flag{display:inline-block;width:9px;height:5px;background:#2c3e8c;margin-right:2px}
.nav{left:147px;top:18px;display:flex;gap:10px;font-size:6.6px;color:#333}
.nav .active{color:var(--purple);border-bottom:1.5px solid var(--purple);padding-bottom:2px}
.nav span{margin-right:3px}

/* hero */
.hero-left{left:0;top:33px;width:188px;height:175px;background:var(--purple)}
.hero-photo{left:188px;top:33px;width:187px;height:175px;background:linear-gradient(90deg,#3d4a52 0%,#4d6670 40%,#567682 100%)}
.hero-title{left:39px;top:73px;color:var(--white);font-size:22px;font-weight:600;line-height:27px;letter-spacing:.3px}
.hero-title .mark{display:inline-block;width:3px;height:16px;background:var(--pink);margin-right:3px;vertical-align:-1px}
.picker{display:inline-block;border:1px solid #fff;border-radius:2px;font-size:6px;padding:1px 8px;line-height:12px;vertical-align:5px;margin-left:6px;letter-spacing:.5px}

/* intro */
.intro-title{left:41px;top:219px;font-size:9.4px;color:var(--purple);font-weight:500}
.intro-rule{left:41px;top:235px;width:41px;height:2px;background:var(--purple)}
.intro-copy{left:41px;top:246px;width:295px;font-size:5.6px;line-height:13.5px;color:#666}
.intro-copy p+p{margin-top:13.5px}

/* band */
.band{left:0;top:375px;width:375px;height:93px;background:var(--purple)}
.band-text{left:20px;right:20px;top:397px;text-align:center;color:#fff;font-size:9.3px;line-height:12px;font-weight:400}

/* benefits */
.benefits{left:68px;top:482px;font-size:6.2px;color:#333;list-style:none}
.benefits li{height:16.6px}
.benefits li::before{content:"•";margin-right:5px;color:#999}

/* video */
.video{left:0;top:590px;width:375px;height:152px;background:radial-gradient(ellipse at 50% 50%,#3a3a3a 0%,#141414 45%,#050505 100%)}
.video-title{top:630px;color:#fff;font-size:9px;font-weight:600}
.video-title span{color:var(--yellow)}
.play{left:162px;top:653px}
.video-list{left:156px;top:686px;color:#ddd;font-size:5.6px;line-height:8.5px;list-style:none}
.video-list li::before{content:"•";margin-right:5px}

/* work for */
.light{position:absolute;left:0;width:375px;background:var(--light)}
.card{left:92px;top:776px;width:192px;height:78px;background:#fff;border-radius:6px;box-shadow:0 2px 6px rgba(0,0,0,.12)}
.card h3{position:absolute;left:0;right:0;top:36px;text-align:center;font-size:7.5px;color:var(--purple);font-weight:500}
.card p{position:absolute;left:20px;right:20px;top:50px;text-align:center;font-size:5.3px;line-height:8px;color:#777}
.arrow-l{left:62px;top:808px;font-size:7px;color:#777}
.arrow-r{left:305px;top:808px;width:9px;height:9px;border-radius:50%;background:var(--yellow);font-size:6px;text-align:center;line-height:9px;color:#333}

/* talk */
.talk-copy{top:908px;font-size:5.6px;line-height:8px;color:#555}
.btn{position:absolute;height:17px;border-radius:3px;font-size:4.6px;font-weight:600;display:flex;align-items:center;justify-content:center;gap:3px;text-transform:uppercase}
.btn-yellow{background:var(--yellow);color:#fff}
.btn-outline{border:1.2px solid var(--purple);color:var(--purple);background:#fff}
.btn-outline i{display:inline-block;width:1.5px;height:9px;background:var(--purple)}

/* numbers */
.ratio{left:71px;top:997px}
.ratio-text{left:172px;top:1022px;font-size:7px;line-height:10px;color:#444;width:130px}

/* cases */
.case{position:absolute;width:144px;height:100px;border-radius:5px;overflow:hidden}
.case .photo{position:absolute;inset:0}
.case .box{position:absolute;left:31px;top:21px;width:82px;height:58px;background:rgba(40,40,40,.75);border-radius:4px;color:#fff;font-size:4.6px;line-height:5.6px;text-align:center;padding-top:12px}
.case .box b{display:block;color:var(--yellow);font-size:6px;font-weight:600;margin:3px 0}
.btn-more{left:154px;top:1355px;width:68px;height:19px;background:var(--yellow);border-radius:3px;color:#fff;font-size:4.4px;font-weight:700;display:flex;align-items:center;justify-content:center;gap:2px}
.btn-more i{display:inline-block;width:1.5px;height:10px;background:#fff}

/* insights */
.post{position:absolute;top:1412px;width:70px;height:94px;background:#fff;border-radius:3px;box-shadow:0 1px 3px rgba(0,0,0,.1);overflow:hidden}
.post .thumb{height:61px}
.post p{font-size:3.8px;line-height:5px;padding:5px 8px 0;color:#222}
.post span{display:block;width:12px;height:1.2px;background:var(--yellow);margin:2px 8px}
.dots{left:171px;top:1513px;display:flex;gap:5px}
.dots i{width:2.5px;height:2.5px;border-radius:50%;background:#ccc}
.dots i:first-child{background:#333}

/* map */
.map{left:42px;top:1548px;width:294px;height:125px;border-radius:8px;background:linear-gradient(180deg,#aed3df,#a3cad6)}
.zoom{left:45px;top:1551px;width:8px;height:14px;background:#fff;border:.5px solid #bbb;font-size:5px;line-height:7px;text-align:center}

/* offices */
.offices{left:0;top:1674px;width:375px;height:82px;background:var(--purple)}
.office{position:absolute;top:1682px;color:#fff;font-size:5.4px;line-height:11.7px}
.office h4{color:var(--yellow);font-size:5.4px;font-weight:600}

/* footer */
.fcol{position:absolute;top:1767px;font-size:4.6px;line-height:10.6px;color:#888}
.fcol h5{font-size:5.4px;color:#222;font-weight:600;line-height:9px}
.fbtn{position:absolute;left:269px;width:62px;height:15px;border-radius:3px;font-size:4px;font-weight:600;display:flex;align-items:center;justify-content:center;gap:3px}
.footer-line{left:40px;top:1833px;width:296px;height:.6px;background:#ddd}
.legal{top:1838px;font-size:3.6px;color:#777}
</style>
</head>
<body>
<div class="page">

  <!-- header -->
  <div class="abs brand">Brevka</div>
  <div class="abs util"><span>Contact Us</span><span><i class="flag"></i>0118 496 0720</span></div>
  <nav class="abs nav"><span class="active">Client</span><span>Case studies</span><span>Services</span><span>Blog</span><span>About Us</span></nav>

  <!-- hero -->
  <div class="abs hero-left"></div>
  <div class="abs hero-photo" role="img" aria-label="Photo of a slate blue panelled front door with a keypad lock"></div>
  <h1 class="abs hero-title"><span class="mark"></span>DEAL<br>ORIGINATION<br>FOR<span class="picker">--YOU?-- &#9662;</span></h1>

  <!-- intro -->
  <h2 class="abs intro-title">Exclusive Deals, Reduced Risk, Stronger Leverage</h2>
  <div class="abs intro-rule"></div>
  <div class="abs intro-copy">
    <p>We consistently deliver high-quality deals, bypassing the crowded open market. Imagine a pipeline filled with precise targets, aligned with your acquisition goals. Our approach minimises execution risk. We bring forward only well-matched prospects backed by transparent tracking and guidance. By specialising in off-market exclusivity, we enhance your negotiation leverage, reducing competition and securing favourable terms for both parties.</p>
    <p>We focus on quality over quantity, building high-trust seller relationships. Gain a competitive edge with our deep market knowledge and highly targeted outreach, expanding your market share. Brevka enables you to acquire smarter, faster, and more effectively.</p>
  </div>

  <!-- band -->
  <div class="abs band"></div>
  <p class="abs band-text">Exclusive Deals, Reduced Risk, Stronger Leverage<br>Brevka empowers acquirers to outpace competitors by<br>consistently delivering high-response, off-market deal<br>flow, without adding headcount or overhead.</p>
  <div class="rule" style="top:451px"></div>

  <!-- benefits -->
  <ul class="abs benefits">
    <li>Find the ideal fit – Target businesses that match your exact criteria</li>
    <li>More options – Access businesses that aren't publicly listed</li>
    <li>No noise – Avoid disruption from advisors and brokers</li>
    <li>Higher-quality deals – Engage with owners who prefer a discreet sale</li>
    <li>More control – Move at your own pace, without broker pressure</li>
    <li>Stronger relationships – Direct contact with business owners</li>
  </ul>

  <!-- video -->
  <div class="abs video" role="img" aria-label="Dark close-up photo of a padlock used as a video backdrop"></div>
  <h2 class="abs center video-title">Unlock <span>Exclusive</span> Opportunities</h2>
  <svg class="abs play" width="34" height="34" viewBox="0 0 34 34"><circle cx="17" cy="17" r="15" fill="#5a1f66" stroke="#c23ad6" stroke-width="2.5"/><circle cx="17" cy="17" r="9" fill="#fff"/><path d="M14.5 12.5 L21.5 17 L14.5 21.5Z" fill="#5a1f66"/></svg>
  <ul class="abs video-list"><li>Exclusive Deals</li><li>Reduced Risk</li><li>Stronger Leverage</li></ul>

  <!-- we work for -->
  <div class="light" style="top:742px;height:128px"></div>
  <h2 class="section-title" style="top:754px">We Work For</h2>
  <div class="rule" style="top:769px;width:28px;left:173.5px"></div>
  <div class="abs arrow-l">&#8249;</div>
  <div class="abs card"><h3>Private Equity</h3><p>Expand your pipeline beyond traditional brokers and geographic boundaries.</p></div>
  <div class="abs arrow-r">&#8250;</div>

  <!-- let's talk -->
  <h2 class="section-title" style="top:883px;color:#333;font-weight:400">If You Want Ideal Flow, <b>Let's Talk</b></h2>
  <div class="rule" style="top:898px"></div>
  <p class="abs center talk-copy">There is only so much you can tell from reviewing our website,<br>the best way to explore is to have a short meeting with one of our team.</p>
  <div class="btn btn-yellow" style="left:121px;top:934px;width:61px"><svg width="5" height="5" viewBox="0 0 10 10"><path d="M2 1l2 2-1 1.5a6 6 0 0 0 2.5 2.5L7 6l2 2-1.5 1.5C4 9 1 6 .5 2.5Z" fill="#fff"/></svg>Call 0118 496 0720</div>
  <div class="btn btn-outline" style="left:193px;top:934px;width:63px"><i></i>Contact Brevka</div>

  <!-- numbers -->
  <div class="light" style="top:966px;height:129px"></div>
  <h2 class="section-title" style="top:978px">Brevka the Numbers</h2>
  <div class="rule" style="top:993px"></div>
  <svg class="abs ratio" width="88" height="88" viewBox="0 0 88 88">
    <circle cx="44" cy="44" r="43" fill="#fff" stroke="#e2e2e2" stroke-width=".8"/>
    <path d="M44 1 A43 43 0 0 0 44 87 Z" fill="var(--purple)"/>
    <circle cx="44" cy="44" r="21" fill="var(--purple)" stroke="#fff" stroke-width="1.5"/>
    <text x="44" y="51" text-anchor="middle" font-family="Poppins,sans-serif" font-size="18" font-weight="600" fill="#fff">1:5</text>
  </svg>
  <p class="abs ratio-text">For every 1 target approached, we analyse at least 5 companies</p>

  <!-- case studies -->
  <div class="light" style="top:1218px;height:162px"></div>
  <h2 class="section-title" style="top:1107px;color:#333;font-weight:400">Recent <b>Case Studies</b></h2>
  <div class="rule" style="top:1122px"></div>
  <div class="case" style="left:42px;top:1137px"><div class="photo" role="img" aria-label="Photo of a wall-mounted fire alarm panel" style="background:linear-gradient(135deg,#c9c9c9,#9e9e9e)"></div><div class="box">Fire Safety Focussed<br>Investment Group<b>Acquired</b>A bespoke Fire and Security<br>Solutions Business</div></div>
  <div class="case" style="left:193px;top:1137px"><div class="photo" role="img" aria-label="Aerial photo of a construction site with workers" style="background:linear-gradient(135deg,#8c8f94,#b8b9bb)"></div><div class="box">Leading Labour<br>Recruitment Company<b>Acquired</b>An Established Construction<br>&amp; Recruitment Firm</div></div>
  <div class="case" style="left:42px;top:1243px"><div class="photo" role="img" aria-label="Photo of a technician installing a security device" style="background:linear-gradient(135deg,#5a4a44,#c9bfb8)"></div><div class="box">Fire Safety Focussed<br>Investment Group<b>Acquired</b>A bespoke Fire and Security<br>Solutions Business</div></div>
  <div class="case" style="left:193px;top:1243px"><div class="photo" role="img" aria-label="Photo of a business professional in a suit in an office corridor" style="background:linear-gradient(135deg,#3d434a,#9aa0a6)"></div><div class="box">Leading Labour<br>Recruitment Company<b>Acquired</b>An Established Construction<br>&amp; Recruitment Firm</div></div>
  <div class="abs btn-more"><i></i>MORE CASE STUDIES</div>

  <!-- insights -->
  <div class="light" style="top:1380px;height:144px"></div>
  <h2 class="section-title" style="top:1388px">M&amp;A Insights &amp; Latest Trends</h2>
  <div class="rule" style="top:1403px"></div>
  <div class="post" style="left:41px"><div class="thumb" role="img" aria-label="Photo of financial charts on a trading screen" style="background:linear-gradient(135deg,#0f1c2a,#1f6c8c)"></div><p>Why Off Market is Key for the Motivated Buyer</p><span></span></div>
  <div class="post" style="left:117px"><div class="thumb" role="img" aria-label="Photo of a city skyline with location pins" style="background:linear-gradient(180deg,#a9c4d9,#7d7b76)"></div><p>Is There a Suitable Business for Sale Near Me?</p><span></span></div>
  <div class="post" style="left:192px"><div class="thumb" role="img" aria-label="Photo of stacked wooden blocks forming steps" style="background:linear-gradient(180deg,#f2efe9,#e0c58f)"></div><p>5 Ways to Increase Your Chances of Selling Your Business</p><span></span></div>
  <div class="post" style="left:267px"><div class="thumb" role="img" aria-label="Photo of hands working on a laptop" style="background:linear-gradient(135deg,#dfe3e8,#8e9aa6)"></div><p>How to Finance Your Next Business Acquisition</p><span></span></div>
  <div class="abs dots"><i></i><i></i><i></i><i></i><i></i></div>

  <!-- map -->
  <h2 class="section-title" style="top:1528px;font-weight:400;color:var(--purple)">Regional and Cross-Border <span style="color:#333">Deal Makers</span></h2>
  <div class="rule" style="top:1543px"></div>
  <div class="abs map" role="img" aria-label="World map with office markers in the UK and Australia"></div>
  <div class="abs zoom">+<br>−</div>
  <svg class="abs" style="left:262px;top:1566px" width="6" height="9" viewBox="0 0 6 9"><path d="M3 9 C1 5.5 0 4.5 0 3 a3 3 0 0 1 6 0 c0 1.5-1 2.5-3 6Z" fill="#2a6fc9"/><circle cx="3" cy="3" r="1.1" fill="#fff"/></svg>
  <svg class="abs" style="left:324px;top:1605px" width="6" height="9" viewBox="0 0 6 9"><path d="M3 9 C1 5.5 0 4.5 0 3 a3 3 0 0 1 6 0 c0 1.5-1 2.5-3 6Z" fill="#2a6fc9"/><circle cx="3" cy="3" r="1.1" fill="#fff"/></svg>

  <!-- offices -->
  <div class="abs offices"></div>
  <div class="office" style="left:42px"><h4>UK &amp; Europe Office</h4>Second Floor<br>Kestrel Court House<br>Reading<br>RG1 4XY<br>Contact: +44 (0)118 496 0720</div>
  <div class="office" style="left:175px"><h4>APAC Office</h4>7 Harbour Lane<br>Millers Point<br>NSW 2000<br>Australia<br>Contact: +61 (0)491 570 156</div>

  <!-- footer -->
  <div class="fcol" style="left:42px"><h5>Clients</h5>Private Equity<br>Trade Buyers<br>Management Buy In<br>Search Funds<br>Corporate Finance</div>
  <div class="fcol" style="left:126px"><h5>Services</h5>Deal Origination<br>Single Acquisitions<br>Buy and Build<br>Bolt-On Acquisitions<br>Cross Border/International</div>
  <div class="fcol" style="left:207px"><h5>&nbsp;</h5>Acquisition Finance<br>Negotiation Support<br>Due Diligence</div>
  <div class="fcol" style="left:269px"><h5>Contact</h5>+44 (0) 118 496 0720<br><svg width="7" height="7" viewBox="0 0 7 7"><circle cx="3.5" cy="3.5" r="3.5" fill="#2a6fc9"/></svg></div>
  <div class="fbtn" style="top:1800px;border:1px solid var(--purple);color:var(--purple)"><i style="display:inline-block;width:1.3px;height:8px;background:var(--purple)"></i>CONTACT BREVKA</div>
  <div class="fbtn" style="top:1820px;background:var(--yellow);color:#fff">BOOK APPOINTMENT</div>
  <div class="abs footer-line"></div>
  <div class="abs legal" style="left:41px">(C) Brevka All Rights Reserved</div>
  <div class="abs legal" style="left:240px">Policies Terms of Use Privacy Policy &nbsp;&nbsp; Contact Us</div>

</div>
</body>
</html>
```